Postcard needed for expert witness service

Looking for a professional postcard that will be mailed to personal injury lawyers / law firms to introduce my expert witness services.

Target Market(s)

Law firms, personal injury lawyers

Industry/Entity Type

Expert witness, law

Font styles to use
Sans Serif

Requirements
Must have
• Logo: The Frost Counsel [Main Heading]Do you handle snow and ice related slip and falls? Darrel is one of the top snow industry experts in the country! [Following should be in a list type fashion, possibly bulleted]Darrel's credentials: Accredited Winter Practitioner (AWP), past WRTA board member and chair, former NQS 4100 certified snow company owner , 32 years in the industry. (555) 284-3917 NOTES: Postcard will be 4" x 6" Please use both sides however must have room for labels and stamp
Should not have
• Wouldn't suggest using both photos on same side. Honestly, feel free to only use one of the slip and fall photos if it works out better. Thanks!

```html
<!DOCTYPE html>
<html lang="en">
<head>
<meta charset="utf-8">
<title>The Frost Counsel – Postcard</title>
<link rel="stylesheet" href="https://fonts.googleapis.com/css2?family=Bebas+Neue&family=Montserrat:wght@400;500&display=swap">
<style>
  :root{
    --stage:#1b1b1b;
    --navy:#1e2638;
    --gold:#b9a47d;
    --white:#ffffff;
    --ink:#1e2638;
    --line:#111111;
    --badge-grey:#e5e5e5;
    --badge-gold:#c9a640;
  }
  *{box-sizing:border-box;margin:0;padding:0}
  html,body{width:858px;height:1200px;overflow:hidden;background:var(--stage)}
  .canvas{position:relative;width:858px;height:1200px}
  .card{position:absolute;left:66px;width:730px;height:517px;background:var(--white);overflow:hidden}
  .card--front{top:42px}
  .card--back{top:610px;height:516px}
  .card__art{position:absolute;inset:0;width:100%;height:100%}
  .display{font-family:"Bebas Neue",Impact,sans-serif;font-weight:400;line-height:1}
  .body{font-family:"Montserrat",Arial,sans-serif}

  .brand{position:absolute;color:var(--white);font-family:"Montserrat",Arial,sans-serif;font-weight:400;text-align:center;letter-spacing:.04em;line-height:1.05;white-space:nowrap}
  .brand span{display:block}
  .brand--front{left:39px;top:36px;width:196px;font-size:27px}
  .brand--back{left:36px;top:34px;width:140px;font-size:20px}

  .headline{position:absolute;left:36px;top:140px;font-size:48px;line-height:40px;color:var(--white);white-space:nowrap}
  .accent{color:var(--gold)}
  .rule{position:absolute;left:19px;top:270px;width:203px;height:2px;background:linear-gradient(90deg,rgba(255,255,255,0),#c9c5bd 30%,#c9c5bd)}
  .intro{position:absolute;left:36px;top:278px;font-size:16.5px;line-height:16px;color:var(--white);font-weight:500;white-space:nowrap}

  .creds__title{position:absolute;left:36px;top:355px;font-size:34px;color:var(--ink);white-space:nowrap}
  .creds__text{position:absolute;left:36px;top:388px;font-size:11.4px;line-height:13.2px;color:var(--ink);white-space:nowrap}

  .cta{position:absolute;white-space:nowrap}
  .cta__label{font-size:26px;color:var(--ink)}
  .cta__phone{font-size:39px;color:var(--gold)}
  .cta--front{left:39px;top:450px}
  .cta--back{left:36px;top:436px}
  .cta--back .cta__label{color:var(--white);font-size:28px}
  .cta--back .cta__phone{color:var(--white);font-size:43px}

  .badge-mark{position:absolute;left:324px;top:452px;width:128px;height:50px;background:var(--badge-grey)}
  .badge-seal{position:absolute;left:467px;top:448px;width:57px;height:57px;border-radius:50%;background:var(--badge-gold)}

  .slogan{position:absolute;left:36px;top:115px;font-size:68px;line-height:55.5px;color:var(--white)}
  .stamp{position:absolute;left:573px;top:36px;width:119px;height:119px;border:1.5px solid var(--line)}
  .address-line{position:absolute;left:443px;width:250px;height:1.5px;background:var(--line)}
  .address-line--1{top:215px}
  .address-line--2{top:247px}
  .address-line--3{top:280px}
  .address-line--4{top:312px}
</style>
</head>
<body>
<main class="canvas">

  <section class="card card--front">
    <svg class="card__art" viewBox="0 0 730 517" aria-hidden="true">
      <defs>
        <linearGradient id="topPhoto" x1="0" y1="0" x2="1" y2="1">
          <stop offset="0" stop-color="#9c9a98"/>
          <stop offset=".5" stop-color="#4a5670"/>
          <stop offset="1" stop-color="#8d8f93"/>
        </linearGradient>
        <linearGradient id="bottomPhoto" x1="0" y1="0" x2="1" y2="1">
          <stop offset="0" stop-color="#8c8278"/>
          <stop offset=".5" stop-color="#4e4a4f"/>
          <stop offset="1" stop-color="#b7b3ae"/>
        </linearGradient>
      </defs>
      <polygon points="309,0 730,0 730,335 481,335" fill="url(#topPhoto)" role="img" aria-label="Photo of a person slipping and falling on icy steps"/>
      <polygon points="0,0 280,0 468,335 0,335" fill="#1e2638"/>
      <line x1="283" y1="0" x2="425" y2="254" stroke="#b9a47d" stroke-width="1.5"/>
      <polygon points="495,335 730,335 730,517 579,517" fill="url(#bottomPhoto)" role="img" aria-label="Photo of a woman who has fallen on a snowy pavement"/>
      <polygon points="470,335 495,335 545,442" fill="#1e2638"/>
    </svg>

    <div class="brand brand--front"><span>THE FROST</span><span>COUNSEL</span></div>

    <h1 class="headline display">Do you handle<br>snow &amp; ice related<br><span class="accent">slip and falls?</span></h1>
    <div class="rule"></div>
    <p class="intro body">Darrel is one of the top snow<br>industry experts in the country!</p>

    <h2 class="creds__title display">Darrel's Credentials</h2>
    <p class="creds__text body">Accredited Winter Practitioner (AWP), past WRTA board<br>member and chair, former NQS 4100 certified snow<br>company owner , 32 years in the industry.</p>

    <div class="cta cta--front display">
      <div class="cta__label">Call now today!</div>
      <div class="cta__phone">(555) 284-3917</div>
    </div>

    <div class="badge-mark"></div>
    <div class="badge-seal"></div>
  </section>

  <section class="card card--back">
    <svg class="card__art" viewBox="0 0 730 516" aria-hidden="true">
      <polygon points="0,0 300,0 452,516 0,516" fill="#1e2638"/>
    </svg>

    <div class="brand brand--back"><span>THE FROST</span><span>COUNSEL</span></div>

    <h2 class="slogan display">Protecting<br>yourself<br>and<br><span class="accent">seeking<br>justice</span></h2>

    <div class="cta cta--back display">
      <div class="cta__label">Call now today!</div>
      <div class="cta__phone">(555) 284-3917</div>
    </div>

    <div class="stamp"></div>
    <div class="address-line address-line--1"></div>
    <div class="address-line address-line--2"></div>
    <div class="address-line address-line--3"></div>
    <div class="address-line address-line--4"></div>
  </section>

</main>
</body>
</html>
```